Looking for a modern, Professional business card design

We have a simple business card, but are looking for a more modern, professional look. A sample of the basic card is attached as well as the logo. We would also like to add that we offer:
Struggling with your finances?
- Learn to become debt free
- Discover the power of cash
- Control your money instead of it controlling you
Let us help you achieve a new level of financial freedom!
Also, we would like to have a "SPECIAL OFFER!: FREE 30 minute consultation"
Financial Planning

```html
<!DOCTYPE html>
<html lang="en">
<head>
<meta charset="utf-8">
<title>Summit Money Coaching – Business Card</title>
<link href="https://fonts.googleapis.com/css2?family=Arimo:wght@400;700&display=swap" rel="stylesheet">
<style>
  :root {
    --backdrop: #3a3532;
    --card: #1b1b1b;
    --green: #5cb531;
    --green-dark: #3f9c2a;
    --white: #f2f2f2;
    --grey: #9a9a9a;
    --divider: #6d6d6d;
  }
  * { margin: 0; padding: 0; box-sizing: border-box; }
  html, body {
    width: 1200px; height: 787px; overflow: hidden;
    background: var(--backdrop);
    font-family: "Arimo", Arial, sans-serif;
  }
  .stage {
    width: 1200px; height: 787px;
    display: flex; align-items: center; justify-content: center; gap: 40px;
  }
  .card {
    width: 540px; height: 309px;
    background: var(--card);
    border-radius: 4px;
    box-shadow: 0 10px 28px rgba(0,0,0,.45);
    position: relative;
    color: var(--white);
  }

  /* Back side */
  .card-back {
    display: flex; flex-direction: column; align-items: center;
    padding: 30px 30px 0; text-align: center;
  }
  .brand-mark {
    display: flex; align-items: center; gap: 10px;
    font-weight: 700; font-size: 22px; letter-spacing: 1px;
    color: var(--grey); text-transform: uppercase;
  }
  .brand-mark .dot {
    width: 30px; height: 30px; border-radius: 50%; background: var(--grey);
  }
  .pitch-heading {
    margin-top: 34px;
    color: var(--green);
    font-weight: 700; font-size: 17px; letter-spacing: .3px;
  }
  .pitch-lines {
    margin-top: 8px;
    font-size: 14px; line-height: 1.45; color: var(--white);
  }
  .pitch-lines .sep { color: var(--green); padding: 0 4px; }
  .offer {
    margin-top: 16px;
    font-weight: 700; font-size: 16px; letter-spacing: .2px;
  }

  /* Front side */
  .card-front {
    display: flex; align-items: center; padding: 0 30px;
  }
  .front-brand {
    width: 215px;
    display: flex; align-items: center; gap: 10px;
  }
  .front-brand .dot {
    width: 34px; height: 34px; border-radius: 50%; background: var(--green);
    flex: none;
  }
  .front-brand .name {
    font-weight: 700; font-size: 21px; line-height: 1.1;
    color: var(--white); text-transform: uppercase;
  }
  .divider {
    width: 1px; height: 150px; background: var(--divider); margin: 0 22px 0 8px;
  }
  .person-name {
    color: var(--green); font-size: 21px; letter-spacing: .5px;
  }
  .person-title { font-size: 17px; margin-top: 2px; margin-bottom: 14px; }
  .contact-list { list-style: none; }
  .contact-list li {
    display: flex; align-items: center; gap: 10px;
    font-size: 15px; line-height: 1.6;
  }
  .contact-list svg { width: 14px; height: 14px; flex: none; fill: var(--green); }
</style>
</head>
<body>
<main class="stage">
  <section class="card card-back">
    <div class="brand-mark"><span class="dot"></span>Summit Money Coaching</div>
    <h2 class="pitch-heading">STRUGGLING WITH YOUR FINANCES?</h2>
    <p class="pitch-lines">
      Learn to become debt free<span class="sep">•</span>Discover the power of cash<br>
      Control your money instead of it controlling you<br>
      Let us help you achieve a new level of financial freedom!
    </p>
    <p class="offer">SPECIAL OFFER!: FREE 30 minute consultation</p>
  </section>

  <section class="card card-front">
    <div class="front-brand">
      <span class="dot"></span>
      <span class="name">Summit Money<br>Coaching</span>
    </div>
    <div class="divider"></div>
    <div class="person">
      <h1 class="person-name">Daniel R. Hayes</h1>
      <p class="person-title">Personal Financial Coach</p>
      <ul class="contact-list">
        <li>
          <svg viewBox="0 0 14 14" aria-hidden="true"><path d="M3 0h8a1 1 0 0 1 1 1v12a1 1 0 0 1-1 1H3a1 1 0 0 1-1-1V1a1 1 0 0 1 1-1zm1 2v8h6V2zm3 9a1 1 0 1 0 0 2 1 1 0 0 0 0-2z"/></svg>
          (205) 555-0148
        </li>
        <li>
          <svg viewBox="0 0 14 14" aria-hidden="true"><path d="M0 3h14v1L7 8 0 4zM0 5.5l7 4 7-4V12H0z"/></svg>
          daniel@clearpathmoney.com
        </li>
        <li>
          <svg viewBox="0 0 14 14" aria-hidden="true"><circle cx="7" cy="7" r="6.5" fill="none" stroke="#5cb531" stroke-width="1.2"/><path d="M1 7h12M7 .5c-2.5 3-2.5 10 0 13M7 .5c2.5 3 2.5 10 0 13" fill="none" stroke="#5cb531" stroke-width="1"/></svg>
          www.clearpathmoney.com
        </li>
      </ul>
    </div>
  </section>
</main>
</body>
</html>
```